Canola Oil Packing Design for catering industry

Hong Kong based edible oil distributor, we would like to have a new packing design for our canola oil steel tin
Feel: easily let people know that the product is from canada; healthy and fresh feel
This packing is for catering market, like hotel, clubs & restaurants
Size: 4 faces in total = 895mm x 355mm allow 6mm for top and bottom, see steel tin sample attached, each size see same graphic
Final output: please provide both ai and pdf file

Target Market(s)

whole sale catering market

Industry/Entity Type

Catering

Font styles to use
Other font styles liked:
• designer choose

Requirements
Must have
• Brand name: Verhollin
• Product name: Canola Oil
• "HACCP certified" wording with icon
• Nutrition information: see file, please use the content and make it look nice, make it looks more or less the same as USA BRQ format: http://www.pelmarquist.org/Items/AdvisoryNotes/ReferencePagesGuideArchiveMaterial/PanelFormats/ref482173.htm
• Product info: see file, please use the content and make it look nice
Nice to have
• canada feel or even canada flag
Should not have
• copy from the others please

```html
<!DOCTYPE html>
<html lang="en">
<head>
<meta charset="utf-8">
<title>Verhollin Canola Oil – Four-Side Tin Wrap</title>
<link href="https://fonts.googleapis.com/css2?family=Archivo:wght@400;600;800;900&family=Roboto+Condensed:wght@400;700&family=Satisfy&display=swap" rel="stylesheet">
<style>
  :root{
    --bg:#e4e4e4;
    --white:#ffffff;
    --red:#c8102e;
    --red-deep:#8e0a1f;
    --gold:#f2b705;
    --gold-light:#ffe27a;
    --amber:#d98a00;
    --green:#4f8a2b;
    --green-light:#a6cf6b;
    --green-dark:#2f5a18;
    --ink:#1a1a1a;
    --grey:#6b6b6b;
    --trim:#9a9a9a;
  }
  *{box-sizing:border-box;margin:0;padding:0}
  html,body{width:900px;height:1200px;overflow:hidden;background:var(--bg)}
  body{font-family:"Archivo",Arial,sans-serif;color:var(--ink);position:relative}

  /* 895 x 355 mm wrap → 860 x 341 px, four equal faces */
  .wrap{position:absolute;left:20px;top:430px;width:860px;height:341px;display:flex;
    box-shadow:0 6px 20px rgba(0,0,0,.18)}
  .face{position:relative;width:215px;height:341px;background:var(--white);overflow:hidden}
  .face + .face{border-left:1px dashed var(--trim)}
  .bleed{position:absolute;left:0;width:100%;height:0;border-top:1px solid var(--trim)}
  .bleed.top{top:6px}
  .bleed.bottom{bottom:6px}

  /* shared bands */
  .top-strip{position:absolute;top:6px;left:0;width:100%;height:44px}
  .brand-band{position:absolute;top:50px;left:0;width:100%;height:92px;
    background:linear-gradient(180deg,var(--red) 0%,var(--red) 72%,var(--red-deep) 100%)}
  .oil-splash{position:absolute;left:0;top:126px;width:100%;height:92px;
    background:radial-gradient(ellipse 75% 55% at 55% 50%,var(--gold-light) 0%,var(--gold) 45%,var(--amber) 80%,rgba(217,138,0,0) 100%)}
  .salad{position:absolute;left:0;top:226px;width:100%;height:109px;
    background:radial-gradient(ellipse at 40% 40%,var(--green-light) 0%,var(--green) 60%,var(--green-dark) 100%)}
  .cert-badge{position:absolute;right:12px;bottom:16px;width:22px;height:16px;background:var(--green);border:1.5px solid var(--white)}

  /* front face */
  .haccp{position:absolute;left:10px;top:8px;display:flex;align-items:center;gap:4px}
  .haccp-seal{width:26px;height:26px;border-radius:50%;background:var(--red)}
  .haccp-label{font-weight:800;font-size:6.5px;color:var(--red);line-height:1.15;text-transform:uppercase}
  .origin{position:absolute;right:10px;top:12px;display:flex;align-items:center;gap:4px}
  .origin-mark{width:8px;height:8px;background:var(--red)}
  .origin-text{font-family:"Roboto Condensed",sans-serif;font-size:6px;color:var(--red);line-height:1.2}
  .brand-name{position:absolute;left:12px;top:8px;font-weight:900;font-size:30px;color:var(--white);letter-spacing:-.5px;line-height:1}
  .claims{position:absolute;left:14px;top:46px;font-family:"Satisfy",cursive;font-size:10px;color:var(--gold-light);line-height:1.25}
  .product-name{position:absolute;right:12px;top:206px;font-weight:800;font-size:19px;color:var(--red);line-height:1}

  /* info face */
  .info-text{position:absolute;left:10px;top:6px;width:195px;font-family:"Roboto Condensed",sans-serif;font-size:5.6px;line-height:1.35;color:var(--ink)}
  .info-text b{color:var(--red)}
  .info-brand{position:absolute;left:10px;top:10px;font-weight:900;font-size:22px;color:var(--white);letter-spacing:-.4px;line-height:1}
  .info-product{position:absolute;left:10px;top:36px;font-weight:800;font-size:13px;color:var(--white)}
  .info-face .oil-splash{width:120px}
  .info-face .salad{width:120px}
  .nutrition{position:absolute;right:8px;top:64px;width:84px;background:var(--white);border:1px solid var(--ink);
    padding:3px 4px;font-size:5px;line-height:1.25}
  .nutrition h3{font-weight:900;font-size:9.5px;line-height:1;border-bottom:.5px solid var(--ink);padding-bottom:1px}
  .serving{padding:1px 0;border-bottom:3px solid var(--ink)}
  .nf-row{display:flex;justify-content:space-between;border-bottom:.5px solid var(--ink);padding:1px 0}
  .nf-row.indent{padding-left:5px}
  .nf-row.thick{border-bottom:2px solid var(--ink)}
  .nf-row.cal{font-weight:900;font-size:7px}
  .nf-dv{font-weight:800;text-align:right;border-bottom:.5px solid var(--ink);padding:1px 0}
  .nf-foot{font-size:4px;padding-top:2px;color:var(--grey)}
</style>
</head>
<body>
<main class="wrap">

  <!-- face 1: front -->
  <section class="face front-face">
    <span class="bleed top"></span><span class="bleed bottom"></span>
    <div class="top-strip">
      <div class="haccp"><span class="haccp-seal"></span><span class="haccp-label">HACCP<br>Certified</span></div>
      <div class="origin"><span class="origin-mark"></span><span class="origin-text">Product of Canada<br>Produit du Canada</span></div>
    </div>
    <div class="brand-band">
      <div class="brand-name">Verhollin</div>
      <div class="claims">No Preservatives<br>Cholesterol Free<br>100% Natural</div>
    </div>
    <div class="oil-splash" role="img" aria-label="Golden canola oil splash"></div>
    <div class="salad" role="img" aria-label="Fresh green salad with vegetables"></div>
    <div class="product-name">Canola Oil</div>
    <span class="cert-badge"></span>
  </section>

  <!-- face 2: information -->
  <section class="face info-face">
    <span class="bleed top"></span><span class="bleed bottom"></span>
    <div class="top-strip">
      <p class="info-text"><b>Ingredients:</b> 100% Canola Oil. <b>Net Volume:</b> 18 L. Pressed from selected Canadian canola seed. Light taste for frying, baking and dressings. <b>Storage:</b> Keep cool, dry and away from sunlight.</p>
    </div>
    <div class="brand-band">
      <div class="info-brand">Verhollin</div>
      <div class="info-product">Canola Oil</div>
    </div>
    <div class="oil-splash" role="img" aria-label="Golden canola oil splash"></div>
    <div class="salad" role="img" aria-label="Fresh green salad with vegetables"></div>
    <div class="nutrition">
      <h3>Nutrition Facts</h3>
      <div class="serving">Serving Size 1 tbsp (14g)</div>
      <div class="nf-row cal thick"><span>Calories</span><span>120</span></div>
      <div class="nf-dv">% Daily Value*</div>
      <div class="nf-row"><span><b>Total Fat</b> 14g</span><span><b>22%</b></span></div>
      <div class="nf-row indent"><span>Saturated Fat 1g</span><span><b>5%</b></span></div>
      <div class="nf-row indent"><span>Trans Fat 0g</span><span></span></div>
      <div class="nf-row"><span><b>Cholesterol</b> 0mg</span><span><b>0%</b></span></div>
      <div class="nf-row"><span><b>Sodium</b> 0mg</span><span><b>0%</b></span></div>
      <div class="nf-row"><span><b>Total Carb.</b> 0g</span><span><b>0%</b></span></div>
      <div class="nf-row thick"><span><b>Protein</b> 0g</span><span></span></div>
      <div class="nf-row"><span>Vitamin E</span><span>15%</span></div>
      <div class="nf-foot">*Based on a 2,000 calorie diet.</div>
    </div>
    <span class="cert-badge"></span>
  </section>

  <!-- face 3: front -->
  <section class="face front-face">
    <span class="bleed top"></span><span class="bleed bottom"></span>
    <div class="top-strip">
      <div class="haccp"><span class="haccp-seal"></span><span class="haccp-label">HACCP<br>Certified</span></div>
      <div class="origin"><span class="origin-mark"></span><span class="origin-text">Product of Canada<br>Produit du Canada</span></div>
    </div>
    <div class="brand-band">
      <div class="brand-name">Verhollin</div>
      <div class="claims">No Preservatives<br>Cholesterol Free<br>100% Natural</div>
    </div>
    <div class="oil-splash" role="img" aria-label="Golden canola oil splash"></div>
    <div class="salad" role="img" aria-label="Fresh green salad with vegetables"></div>
    <div class="product-name">Canola Oil</div>
    <span class="cert-badge"></span>
  </section>

  <!-- face 4: information -->
  <section class="face info-face">
    <span class="bleed top"></span><span class="bleed bottom"></span>
    <div class="top-strip">
      <p class="info-text"><b>Ingredients:</b> 100% Canola Oil. <b>Net Volume:</b> 18 L. Pressed from selected Canadian canola seed. Light taste for frying, baking and dressings. <b>Storage:</b> Keep cool, dry and away from sunlight.</p>
    </div>
    <div class="brand-band">
      <div class="info-brand">Verhollin</div>
      <div class="info-product">Canola Oil</div>
    </div>
    <div class="oil-splash" role="img" aria-label="Golden canola oil splash"></div>
    <div class="salad" role="img" aria-label="Fresh green salad with vegetables"></div>
    <div class="nutrition">
      <h3>Nutrition Facts</h3>
      <div class="serving">Serving Size 1 tbsp (14g)</div>
      <div class="nf-row cal thick"><span>Calories</span><span>120</span></div>
      <div class="nf-dv">% Daily Value*</div>
      <div class="nf-row"><span><b>Total Fat</b> 14g</span><span><b>22%</b></span></div>
      <div class="nf-row indent"><span>Saturated Fat 1g</span><span><b>5%</b></span></div>
      <div class="nf-row indent"><span>Trans Fat 0g</span><span></span></div>
      <div class="nf-row"><span><b>Cholesterol</b> 0mg</span><span><b>0%</b></span></div>
      <div class="nf-row"><span><b>Sodium</b> 0mg</span><span><b>0%</b></span></div>
      <div class="nf-row"><span><b>Total Carb.</b> 0g</span><span><b>0%</b></span></div>
      <div class="nf-row thick"><span><b>Protein</b> 0g</span><span></span></div>
      <div class="nf-row"><span>Vitamin E</span><span>15%</span></div>
      <div class="nf-foot">*Based on a 2,000 calorie diet.</div>
    </div>
    <span class="cert-badge"></span>
  </section>

</main>
</body>
</html>
```